Business Card Design

Provide project management services to the construction and other industries
Construction services - Civil and Concrete works
Shop Detailing
Structural Modelling
Client side coordination of project teams and consultants
Feasibility Studies for construction projects

Industry/Entity Type

Business

Contact Information for Business Card

Crestline Ops
Darrel Pikett B.Sc (Eng), M.P.M.
Director

m: 0412 583 716
e: dpikett@crestlineops.com.au

p: 08 6293 4078
a: 17 Bramblewood Court, Stirling, WA 6021

```html
<!DOCTYPE html>
<html lang="en">
<head>
<meta charset="utf-8">
<title>Crestline Ops – Business Card</title>
<link rel="stylesheet" href="https://fonts.googleapis.com/css2?family=Arimo:ital,wght@1,400&family=Noto+Serif&family=Open+Sans:wght@400;800&display=swap">
<style>
  :root {
    --backdrop: #060808;
    --card: #ffffff;
    --ink: #111111;
    --logo-ink: #2b2b2b;
    --rule-yellow: #f2c300;
    --glow-yellow: #f6f23a;
    --tower-green: #2fe08a;
    --tower-deep: #0a5a33;
    --photo-sky: #c9d8e6;
    --photo-warm: #efe6a8;
  }
  html, body {
    margin: 0;
    padding: 0;
    width: 998px;
    height: 1200px;
    overflow: hidden;
    background: var(--backdrop);
  }
  .sheet {
    position: absolute;
    top: 0;
    left: 0;
    width: 1125px;
    height: 1353px;
    transform: scale(0.8871);
    transform-origin: 0 0;
  }
  .sheet-art {
    position: absolute;
    inset: 0;
  }
  .card-text {
    position: absolute;
    margin: 0;
    white-space: nowrap;
    color: var(--ink);
  }
  .brand {
    font-family: "Open Sans", sans-serif;
    font-weight: 800;
    color: var(--logo-ink);
    letter-spacing: -1px;
    line-height: 1;
  }
  .front-brand { right: 195px; top: 88px; font-size: 58px; }
  .back-brand { left: 190px; top: 752px; font-size: 78px; }
  .person {
    font-family: "Arimo", sans-serif;
    font-style: italic;
    text-align: right;
    right: 200px;
    line-height: 1;
  }
  .person-name { top: 155px; font-size: 32px; }
  .person-quals { top: 197px; font-size: 22px; }
  .person-role { top: 220px; font-size: 38px; right: 198px; }
  .contact {
    font-family: "Noto Serif", serif;
    left: 90px;
    line-height: 1;
  }
  .contact-address { top: 414px; font-size: 27px; line-height: 36px; }
  .contact-phone { top: 490px; font-size: 41px; line-height: 40px; letter-spacing: 1px; }
  .contact-email { top: 570px; font-size: 32px; }
  .services {
    position: absolute;
    left: 235px;
    top: 852px;
    margin: 0;
    padding: 0;
    list-style: none;
    font-family: "Open Sans", sans-serif;
    font-size: 26px;
    color: var(--ink);
  }
  .services li { line-height: 37px; height: 46px; }
  .services li.two-line { height: 83px; }
  .back-email {
    font-family: "Noto Serif", serif;
    left: 227px;
    top: 1166px;
    font-size: 44px;
    line-height: 1;
  }
</style>
</head>
<body>
<main class="sheet">
  <svg class="sheet-art" width="1125" height="1353" viewBox="0 0 1125 1353">
    <defs>
      <linearGradient id="tower-fill" x1="0" y1="0" x2="1" y2="1">
        <stop offset="0" stop-color="var(--tower-deep)"/>
        <stop offset="0.5" stop-color="var(--tower-green)"/>
        <stop offset="1" stop-color="var(--tower-deep)"/>
      </linearGradient>
      <linearGradient id="front-photo" x1="0" y1="0" x2="1" y2="0.6">
        <stop offset="0" stop-color="var(--photo-sky)" stop-opacity="0.8"/>
        <stop offset="0.35" stop-color="#ffffff" stop-opacity="0.4"/>
        <stop offset="0.7" stop-color="var(--photo-warm)"/>
        <stop offset="1" stop-color="#9aa6b4"/>
      </linearGradient>
      <radialGradient id="front-glow" cx="0.85" cy="0.1" r="0.55">
        <stop offset="0" stop-color="var(--glow-yellow)"/>
        <stop offset="1" stop-color="var(--glow-yellow)" stop-opacity="0"/>
      </radialGradient>
      <radialGradient id="back-glow" cx="0.15" cy="0.1" r="0.6">
        <stop offset="0" stop-color="var(--glow-yellow)"/>
        <stop offset="1" stop-color="var(--glow-yellow)" stop-opacity="0"/>
      </radialGradient>
      <linearGradient id="back-photo" x1="0" y1="0" x2="1" y2="1">
        <stop offset="0" stop-color="#ffffff" stop-opacity="0"/>
        <stop offset="1" stop-color="#aab4bd" stop-opacity="0.55"/>
      </linearGradient>
      <linearGradient id="rule" x1="0" y1="0" x2="1" y2="0">
        <stop offset="0" stop-color="var(--rule-yellow)"/>
        <stop offset="0.6" stop-color="var(--rule-yellow)" stop-opacity="0.6"/>
        <stop offset="1" stop-color="var(--rule-yellow)" stop-opacity="0"/>
      </linearGradient>
      <clipPath id="front-shape">
        <path d="M15 35 H968 L1040 490 Q1045 550 990 565 L300 665 H15 Z"/>
      </clipPath>
      <clipPath id="back-shape">
        <path d="M165 700 H1100 V1330 L300 1270 Q95 1250 95 1160 Z"/>
      </clipPath>
    </defs>

    <rect class="tower-art" x="860" y="30" width="242" height="635" fill="url(#tower-fill)" role="img" aria-label="Green wireframe glass tower illustration"/>
    <rect class="tower-art" x="380" y="560" width="722" height="105" fill="url(#tower-fill)" role="img" aria-label="Green wireframe glass tower illustration"/>

    <path d="M15 35 H968 L1048 490 Q1055 565 995 578 L300 672 H15 Z" fill="#000"/>
    <g clip-path="url(#front-shape)">
      <rect x="15" y="35" width="1030" height="640" fill="var(--card)"/>
      <path d="M35 50 H960 L1032 500 Q1030 550 990 556 L620 590 Q300 430 35 370 Z" fill="url(#front-photo)" role="img" aria-label="Photo of a business handshake with hard hat, blueprints, spirit level, tape measure and laptop"/>
      <rect x="500" y="35" width="545" height="330" fill="url(#front-glow)"/>
    </g>

    <rect class="tower-art" x="12" y="697" width="200" height="634" fill="url(#tower-fill)" role="img" aria-label="Green wireframe glass tower illustration"/>
    <rect class="tower-art" x="200" y="1240" width="700" height="91" fill="url(#tower-fill)" role="img" aria-label="Green wireframe glass tower illustration"/>

    <path d="M150 700 H1100 V1335 L300 1280 Q78 1258 82 1160 Z" fill="#000"/>
    <g clip-path="url(#back-shape)">
      <rect x="80" y="700" width="1020" height="640" fill="var(--card)"/>
      <rect x="160" y="700" width="560" height="300" fill="url(#back-glow)"/>
      <path d="M640 900 H1100 V1330 L700 1300 Z" fill="url(#back-photo)" role="img" aria-label="Faded photo of hard hat, blueprints, tape measure and laptop"/>
    </g>

    <g class="service-rules" fill="url(#rule)">
      <rect x="230" y="927" width="470" height="7"/>
      <rect x="230" y="973" width="470" height="7"/>
      <rect x="230" y="1019" width="400" height="7"/>
      <rect x="230" y="1065" width="400" height="7"/>
      <rect x="230" y="1111" width="560" height="7"/>
      <rect x="230" y="1157" width="560" height="7"/>
    </g>
  </svg>

  <p class="card-text brand front-brand">CRESTLINE OPS</p>
  <p class="card-text person person-name">Darrel Pikett</p>
  <p class="card-text person person-quals">B.Sc (Eng), M.P.M.</p>
  <p class="card-text person person-role">Director</p>
  <p class="card-text contact contact-address">17 Bramblewood Court,<br>Harwood, WA 608</p>
  <p class="card-text contact contact-phone">0412 583 716<br>08 6293 4078</p>
  <p class="card-text contact contact-email">dpikett@crestlineops.com.au</p>

  <p class="card-text brand back-brand">CRESTLINE OPS</p>
  <ul class="services">
    <li class="two-line">Provide project management services to the construction<br>and other industries</li>
    <li>Construction services - Civil and Concrete works</li>
    <li>Shop Detailing</li>
    <li>Structural Modelling</li>
    <li>Client side coordination of project teams and consultants</li>
    <li>Feasibility Studies for construction projects</li>
  </ul>
  <p class="card-text back-email">dpikett@crestlineops.com.au</p>
</main>
</body>
</html>
```